Real Estate Open House & For Sale Signage

I am designing brand new signs for my real estate company. All I have so far are my logo and a business card design. I would like to have designed two different signs, 1. Open House directional sign, 2. For Sale Company sign. Both signs need to will be eye catching from the street, easy to read, identifiable and memorable.

Target Market(s)

Males & females, Ages between 30-65, affluent, educated, professionals.

Industry/Entity Type

Real Estate

Font styles to use
Serif
Sans Serif

Colors
33b8a4
34a7d8
acd137
3277b5

Requirements
Must have
• Must have my company logo & real estate license number visible on the sign. Must be easily visible and eye catching from a moving vehicle. Must have a professional and trustworthy appeal. Must bring to mind real estate.
Nice to have
• Image or icon that will denote real estate and be known as a part of my company identity and marketing theme.
Should not have
• Attached is a feeble attempt at creating my For Sale sign. The information on the sign is accurate, but the design is not appealing to me at all. It feels very amateurish.

```html
<!DOCTYPE html>
<html lang="en">
<head>
<meta charset="utf-8">
<title>Kaimana Realty Partners – Signage</title>
<link rel="stylesheet" href="https://fonts.googleapis.com/css2?family=Open+Sans:wght@400;600&display=swap">
<style>
  :root {
    --green: #9ecb3b;
    --blue: #1589c0;
    --blue-light: #9abfe0;
    --ink-blue: #1a8ac4;
    --white: #ffffff;
    --frame: #c9c9c9;
  }
  html, body {
    margin: 0;
    padding: 0;
    overflow: hidden;
  }
  body {
    width: 771px;
    height: 1200px;
    background: var(--white);
    position: relative;
    font-family: "Open Sans", sans-serif;
  }
  .sign {
    position: absolute;
    left: 50px;
    width: 655px;
    height: 493px;
    box-sizing: border-box;
    border: 1px solid var(--frame);
    background: var(--white);
    overflow: hidden;
  }
  .sign--sale { top: 50px; }
  .sign--open { top: 638px; }
  .sign__shapes {
    position: absolute;
    left: 0;
    top: 0;
    width: 655px;
    height: 493px;
  }
  .brand {
    position: absolute;
    right: 85px;
    top: 98px;
    margin: 0;
    color: var(--green);
    font-weight: 600;
    font-size: 28px;
    line-height: 1.05;
    letter-spacing: 3px;
    text-align: right;
  }
  .sign__headline {
    position: absolute;
    right: 85px;
    top: 200px;
    height: 87px;
    margin: 0;
    color: var(--white);
    font-weight: 600;
    font-size: 66px;
    line-height: 87px;
    white-space: nowrap;
  }
  .sign__tagline {
    position: absolute;
    left: 88px;
    top: 312px;
    margin: 0;
    height: 35px;
    line-height: 35px;
    color: var(--white);
    font-size: 16px;
    font-weight: 400;
  }
  .agent {
    position: absolute;
    right: 85px;
    top: 376px;
    margin: 0;
    color: var(--ink-blue);
    font-size: 16px;
    text-align: right;
  }
  .phone {
    position: absolute;
    right: 83px;
    top: 392px;
    margin: 0;
    color: var(--ink-blue);
    font-size: 63px;
    font-weight: 400;
    line-height: 80px;
    white-space: nowrap;
  }
</style>
</head>
<body>

<section class="sign sign--sale" aria-label="For sale sign">
  <svg class="sign__shapes" viewBox="0 0 655 493" aria-hidden="true">
    <polygon fill="var(--green)" points="45,176 45,166 133,62 218,166 608,166 608,176"/>
    <polygon fill="var(--blue)" points="150,176 190,98 258,176"/>
    <rect fill="var(--green)" x="45" y="311" width="563" height="37"/>
    <rect fill="var(--blue)" x="0" y="174" width="655" height="138"/>
    <polygon fill="var(--blue-light)" points="90,201 155,123 222,201"/>
    <rect fill="var(--blue-light)" x="55" y="200" width="545" height="87"/>
  </svg>
  <p class="brand">KAIMANA<br>REALTY</p>
  <h1 class="sign__headline">FOR SALE</h1>
  <p class="sign__tagline">YOUR NEIGHBOURHOOD SPECIALIST</p>
  <p class="agent">LEILANI HART: RB-20451</p>
  <p class="phone">(808) 555 01 42</p>
</section>

<section class="sign sign--open" aria-label="Open house sign">
  <svg class="sign__shapes" viewBox="0 0 655 493" aria-hidden="true">
    <polygon fill="var(--green)" points="45,176 45,166 133,62 218,166 608,166 608,176"/>
    <polygon fill="var(--blue)" points="150,176 190,98 258,176"/>
    <rect fill="var(--green)" x="45" y="311" width="563" height="37"/>
    <rect fill="var(--blue)" x="0" y="174" width="655" height="138"/>
    <polygon fill="var(--blue-light)" points="90,201 155,123 222,201"/>
    <rect fill="var(--blue-light)" x="55" y="200" width="545" height="87"/>
  </svg>
  <p class="brand">KAIMANA<br>REALTY</p>
  <h1 class="sign__headline">OPEN HOUSE</h1>
  <p class="sign__tagline">YOUR NEIGHBOURHOOD SPECIALIST</p>
  <p class="agent">LEILANI HART: RB-20451</p>
  <p class="phone">(808) 555 01 42</p>
</section>

</body>
</html>
```